KVT REFRIGERATION HEATING AND COOLING COMPANY IN AUSTRALIA NEEDS A SLEEK AND PROFESSIONAL DESIGN FOR MERANO VANS THERE DIFFERENT OF VANS AVAILABLE ON THE INTERNET BUT PLEASE USE THIS ONE. (VO RUNE LWB pxm307t french vanilla colour it's without window glass screen). SHOULD BE VERY PLEASING TO SEE AND COLOR SCHEME SHOULD BE GREEN and BLUE OR CLOSE TO OUR LOGO.

THE DESIGN SHOULD COMMUNICATE TO THE PEOPLE AND OUR SERVICES AND CONTACT DETAILS SHOULD BE PROMINENT TO SEE.

ALL POPULAR BRANDS LOGOS NEED TO BE PLACED AS WELL. ( PLS CHECK FLYER) OR READ ALL THE BRIEF.

THE EXISTING COLOR OF THE VAN IS WHITE AND CAN/ SHOULD UTILISE THIS NEGATIVE SPACE/COLOR TO BLEND WITH GREEN AND BLUE. WE WELCOME ANY IMPROVISATION ON COLORS SCHEME.

PS
PLEASE FIND THE ATTACHED DOCUMENTS AND TAKE THE LOGOS FROM THE ORIGINAL WEBSITE AND ALSO SEE BUSINESS CARD AND FLYER

CONTACT

0431872264
0419253308
INFO@KVTREFRIGERTION.COM.AU
WWW.KVTREFRIGERATION.COM.AU

_________________________________________________
VAN TEXT
TRUST YOUR EXPERTS— TAG LINE
INSTALLATION, REPAIRS , MAINTENANCE , SALE & SERVICE OF DOMESTIC , COMMERCIAL REFRIGERATION HEATING & AIR CONDITIONING
SAME DAY BOOKING/ 24/7

THESE ARE THE HEATER BRANDS

Talmor ( FIND LOGO WEBSITE
QUENTIS ( FIND LOGO WEBSITE
WELUMAX ( FIND LOGO WEBSITE
Pirsto ( FIND LOGO WEBSITE
Warm tides ( FIND LOGO WEBSITE

THESE ARE THE AIR CONS BRAND
Holvex ( FIND LOGO WEBSITE
Marepol ( FIND LOGO WEBSITE
KELVANORA ( FIND LOGO WEBSITE
Zubrivent ( FIND LOGO WEBSITE
TOSKEL ( FIND LOGO WEBSITE
Dovrack ( FIND LOGO WEBSITE
Zt ( FIND LOGO WEBSITE
Velmo ( FIND LOGO WEBSITE

ACCREDITATION / LOCAL COUNCIL COMPLIANCE AND

AU NUMBER 58704
QNT FIND LOGO ( FIND LOGO WEBSITE
JRP FIND LOGO ( FIND LOGO WEBSITE
Southern Coldtrade Guild FIND LOGO
TIDEWAY PIPEWORK ( FIND LOGO WEBSITE

PLEASE GO THROUGH THE ATTACHED FLYERS TO KNOW WHAT I AM TALKING ABOUT
THANK YOU VERY MUCH FOR YOUR TIME AND EFFORTS TO DESIGN.

Target Market(s)

GENERAL PUBLIC,

Industry/Entity Type

Hvac

Font styles to use
Serif
Sans Serif

Colors
0255a3
9bcb3c
00a990
3277b5

Requirements
Must have
• SEE PROJECT DESCRIPTION
• LEADING AUSTRALIAN BRANDS LOGOS, CONTACT DETAILS,
• OUR COMPANY DETAILS AND LOGOS
Nice to have
• ALL LOGOS CHECK FLYERS,
• SHOULD USE NEGATIVE SPACE AND COLOR
Should not have
• PICTURES, OF ACTUAL PRODUCTS AS IN HEATER AIR CONDITIONING UNITS OR ANY OTHER APPLIANCES

```html
<!DOCTYPE html>
<html lang="en">
<head>
<meta charset="utf-8">
<title>KVT Refrigeration – Van Wrap</title>
<link rel="stylesheet" href="https://fonts.googleapis.com/css2?family=Montserrat:ital,wght@0,600;0,700;0,800;1,700;1,800&family=Merriweather:ital,wght@1,700&display=swap">
<style>
  :root {
    --navy: #0255a3;
    --blue: #3277b5;
    --sky: #4aa3dd;
    --green: #9bcb3c;
    --teal: #00a990;
    --white: #ffffff;
    --body: #f4f5f6;
    --line: #c9ccd0;
    --glass: #4b5563;
    --tyre: #1c1c1e;
    --red: #d0202e;
    --sans: "Montserrat", Arial, sans-serif;
    --serif: "Merriweather", Georgia, serif;
  }
  html, body { margin: 0; padding: 0; overflow: hidden; background: var(--white); }
  .canvas { position: relative; width: 1200px; height: 900px; overflow: hidden; background: var(--white); font-family: var(--sans); }
  .van-art { position: absolute; inset: 0; }

  .brand-name { position: absolute; left: 482px; top: 298px; color: var(--navy); font-weight: 800; line-height: 1; }
  .brand-name .mark { display: block; font-size: 92px; letter-spacing: 2px; }
  .brand-name .sub { display: block; font-size: 16px; letter-spacing: 7px; margin-left: 170px; margin-top: -6px; }
  .brand-dot { position: absolute; left: 740px; top: 296px; width: 92px; height: 92px; border-radius: 50%; background: var(--sky); }

  .services { position: absolute; left: 425px; top: 405px; width: 440px; color: var(--navy); font-style: italic; font-weight: 700; font-size: 10px; letter-spacing: 0.6px; line-height: 13px; text-align: center; }

  .phone { position: absolute; left: 178px; top: 437px; height: 30px; display: flex; align-items: center; gap: 8px; color: var(--white); font-weight: 700; font-size: 20px; letter-spacing: 0.5px; }
  .phone-icon { width: 18px; height: 18px; border-radius: 50%; background: var(--green); display: flex; align-items: center; justify-content: center; }
  .web { position: absolute; left: 430px; top: 437px; height: 30px; display: flex; align-items: center; gap: 8px; color: var(--white); font-weight: 800; font-size: 20px; letter-spacing: 0.3px; }

  .brands { position: absolute; left: 425px; display: flex; gap: 11px; align-items: center; font-weight: 700; font-size: 8px; color: var(--navy); white-space: nowrap; }
  .brands.row-one { top: 485px; }
  .brands.row-two { top: 503px; left: 427px; }
  .brands .red { color: var(--red); }
  .brands .teal { color: var(--teal); }
  .brands .dark { color: #333; }

  .tagline-path { font-family: var(--serif); font-style: italic; font-weight: 700; font-size: 12px; fill: var(--red); }
  .hours { position: absolute; left: 950px; top: 430px; color: var(--white); font-weight: 800; font-size: 30px; line-height: 1; }
  .hours sup { font-size: 16px; }
  .booking { position: absolute; left: 945px; top: 461px; color: var(--white); font-weight: 700; font-size: 9.5px; letter-spacing: 0.3px; }
</style>
</head>
<body>
<main class="canvas">
  <svg class="van-art" width="1200" height="900" viewBox="0 0 1200 900" aria-hidden="false">
    <defs>
      <linearGradient id="sweepBlue" x1="0" y1="0" x2="1" y2="0">
        <stop offset="0" stop-color="#4aa3dd"/>
        <stop offset="0.6" stop-color="#3277b5"/>
        <stop offset="1" stop-color="#0255a3"/>
      </linearGradient>
      <linearGradient id="barGreen" x1="0" y1="0" x2="1" y2="0">
        <stop offset="0" stop-color="#9bcb3c"/>
        <stop offset="1" stop-color="#7fb52a"/>
      </linearGradient>
      <clipPath id="bodyClip">
        <path d="M96,500 L100,440 Q108,392 168,346 L268,258 Q290,240 332,236 L1040,214 Q1082,214 1090,250 L1104,420 L1110,560 Q1108,588 1086,590 L120,596 Q96,594 96,570 Z"/>
      </clipPath>
      <path id="taglineArc" d="M918,312 A62,62 0 0 1 1035,340"/>
    </defs>

    <!-- ground shadow -->
    <ellipse class="ground" cx="600" cy="638" rx="560" ry="12" fill="#e6e6e6"/>

    <!-- van body -->
    <path class="van-body" d="M96,500 L100,440 Q108,392 168,346 L268,258 Q290,240 332,236 L1040,214 Q1082,214 1090,250 L1104,420 L1110,560 Q1108,588 1086,590 L120,596 Q96,594 96,570 Z" fill="var(--body)" stroke="var(--line)" stroke-width="2"/>

    <g clip-path="url(#bodyClip)">
      <!-- roof swooshes -->
      <path class="roof-green" d="M430,232 Q720,200 1110,228 L1110,236 Q760,214 470,240 Z" fill="var(--green)"/>
      <path class="roof-blue" d="M480,236 Q760,220 1110,246 L1110,292 Q900,262 700,262 Q560,262 480,236 Z" fill="url(#sweepBlue)"/>
      <!-- lower swoosh -->
      <path class="lower-green" d="M360,500 Q700,560 1110,380 L1110,396 Q720,574 360,506 Z" fill="var(--green)"/>
      <path class="lower-blue" d="M380,520 Q720,590 1110,400 L1110,600 L380,600 Z" fill="url(#sweepBlue)"/>
      <path class="lower-white" d="M380,546 Q760,606 1110,470" fill="none" stroke="var(--white)" stroke-width="3"/>
      <!-- contact bars -->
      <rect class="web-bar" x="380" y="436" width="640" height="32" fill="url(#barGreen)"/>
      <rect class="phone-bar" x="172" y="436" width="210" height="32" rx="6" fill="var(--blue)"/>
    </g>

    <!-- windows -->
    <path class="cab-window" d="M215,302 Q230,292 250,292 L398,288 Q404,288 404,296 L404,392 L212,396 Z" fill="var(--glass)"/>
    <path class="windscreen" d="M120,420 Q135,385 170,352 L198,330 L198,398 Z" fill="#8b95a1"/>
    <!-- door lines -->
    <path class="door-line" d="M170,300 L170,590 M410,240 L410,590" stroke="var(--line)" stroke-width="1.5" fill="none"/>
    <rect class="door-handle" x="350" y="402" width="36" height="9" rx="4" fill="#d4d7da"/>
    <rect class="headlamp" x="104" y="448" width="54" height="42" rx="6" fill="#d7dade" stroke="#a7adb3"/>
    <rect class="tail-lamp" x="1094" y="420" width="12" height="80" rx="4" fill="#a3212b"/>

    <!-- wheels -->
    <g class="wheel">
      <circle cx="306" cy="578" r="72" fill="#2a2a2c"/>
      <circle cx="306" cy="578" r="48" fill="#cfd3d7"/>
      <circle cx="306" cy="578" r="10" fill="#9aa0a6"/>
    </g>
    <g class="wheel">
      <circle cx="906" cy="578" r="72" fill="#2a2a2c"/>
      <circle cx="906" cy="578" r="48" fill="#cfd3d7"/>
      <circle cx="906" cy="578" r="10" fill="#9aa0a6"/>
    </g>

    <!-- mascot area -->
    <rect class="mascot" x="880" y="300" width="170" height="190" rx="20" fill="#4f86c6" opacity="0.85" role="img" aria-label="Mascot illustration: cheerful technician in blue overalls running with a wrench and a red toolbox"/>

    <!-- tagline arc -->
    <text class="tagline-path"><textPath href="#taglineArc">TRUST YOUR EXPERTS</textPath></text>
  </svg>

  <div class="brand-dot" aria-hidden="true"></div>
  <div class="brand-name">
    <span class="mark">KVT</span>
    <span class="sub">REFRIGERATION</span>
  </div>

  <p class="services" style="margin:0">• INSTALLATION • REPAIRS • MAINTENANCE • SALE &amp; SERVICE OF DOMESTIC<br>• COMMERCIAL REFRIGERATION HEATING &amp; AIR CONDITIONING</p>

  <div class="phone">
    <span class="phone-icon">
      <svg width="11" height="11" viewBox="0 0 24 24"><path d="M6.6 10.8a15.1 15.1 0 0 0 6.6 6.6l2.2-2.2a1 1 0 0 1 1-.25 11.4 11.4 0 0 0 3.6.57 1 1 0 0 1 1 1V20a1 1 0 0 1-1 1A17 17 0 0 1 3 4a1 1 0 0 1 1-1h3.5a1 1 0 0 1 1 1c0 1.25.2 2.45.57 3.6a1 1 0 0 1-.25 1z" fill="#fff"/></svg>
    </span>
    (043)187-2264
  </div>

  <div class="web">
    <svg width="16" height="16" viewBox="0 0 24 24" fill="none" stroke="#fff" stroke-width="2"><circle cx="12" cy="12" r="10"/><path d="M2 12h20M12 2a15 15 0 0 1 0 20M12 2a15 15 0 0 0 0 20"/></svg>
    WWW.KVTREFRIGERATION.COM.AU
  </div>

  <div class="brands row-one">
    <span>Zubrivent</span><span class="red">TOSKEL</span><span>Corvane</span><span class="dark">Talmor</span><span class="red">Thermbay</span><span class="teal">Warm tides</span><span class="teal">Pirsto</span><span class="red">Brintel</span><span>Dovrack</span><span class="dark">WELUMAX</span>
  </div>
  <div class="brands row-two">
    <span>Holvex</span><span class="red">KELVANORA</span><span class="teal">Nuvira</span><span>Aerolis</span><span class="red">Zt</span><span class="red">QUENTIS</span><span class="dark">Corvel</span><span class="red">Marepol</span><span class="red">Halvern</span>
  </div>

  <div class="hours">24<sup>/7</sup></div>
  <div class="booking">SAME DAY BOOKING</div>
</main>
</body>
</html>
```